Defense Attorney Business Card Design Project/ Stationary

I am looking for a distinctive business card design for my solo law practice.
I practice criminal defense, both juvenile and adult, including DUI. I am a very experienced attorney with prior military experience. The design should convey a traditional, old school flair, but not be too stodgy or uptight. Some color. My logo should appear.
Updates

Project Deadline Extended Reason: I misunderstood how this project works and I was not prepared with my logo when this project ran the first time. Added Thursday, November 13, 2014

Project Deadline Extended
Reason: I was sent overseas on military duty last year, which interrupted this project. Thank you for your participation... I hope we can get this done this week! Thank you, Ben

Target Market(s)

Regular everyday people looking for strong, knowledgeable, authoritative representation while they are faced with criminal charges. Many have never been charged with a crime before. A reassuring air is therefore desired.

Industry/Entity Type

Business

Contact Information for Business Card

My information is:
Benedict L. Morrow, Attorney at Law
735 Linden Avenue Suite 400
Oakland, California 94612
Tel: (510) 555-0183
Fax: (510) 555-0147
email: benmorrowlaw@examplemail.test
web: www.benmorrowlaw.test

Font styles to use
Serif
Sans Serif
Decorative

Colors
0255a3
ffffff

Requirements
Must have
• Sharp lines, bold elements. Conservative use of colors, such as deep blues, burgundy, grays for example.
• While my logo says "Ben Morrow", it should be modified to show "Benedict L. Morrow".
Should not have
• Cliche imagery such as scales of justice, gavels, Statue of Liberty, etc.

```html
<!DOCTYPE html>
<html lang="en">
<head>
<meta charset="utf-8">
<title>Benedict L. Morrow Law – Business Card</title>
<link rel="stylesheet" href="https://fonts.googleapis.com/css2?family=Lato:wght@400;700&display=swap">
<style>
  :root {
    --page-bg: #ffffff;
    --front-bg: #2f2d2e;
    --back-bg: #063049;
    --ink-light: #c9cacb;
    --ink-soft: #aeb6bc;
    --accent: #c8923a;
    --rule: #9a9a9a;
  }
  * { margin: 0; padding: 0; box-sizing: border-box; }
  html, body {
    width: 929px;
    height: 1200px;
    overflow: hidden;
    background: var(--page-bg);
  }
  .sheet {
    position: relative;
    width: 929px;
    height: 1200px;
  }
  .card {
    position: absolute;
    top: 29px;
    height: 255px;
  }
  .card-front {
    left: 27px;
    width: 434px;
    background: var(--front-bg);
    border-top-left-radius: 30px;
  }
  .card-back {
    left: 468px;
    width: 435px;
    background: var(--back-bg);
    border-top-right-radius: 30px;
  }
  .brand {
    position: absolute;
    right: 18px;
    top: 150px;
    width: 232px;
    text-align: center;
    color: var(--ink-light);
    font-family: "Lato", Arial, sans-serif;
    font-weight: 700;
  }
  .brand-mark {
    display: block;
    width: 40px;
    height: 40px;
    margin: 0 auto 14px;
    border-radius: 50%;
    background: var(--ink-light);
  }
  .brand-name {
    font-size: 18px;
    line-height: 1;
    padding-bottom: 5px;
    border-bottom: 1px solid var(--rule);
  }
  .brand-tagline {
    margin-top: 5px;
    font-size: 11px;
    letter-spacing: 0.3px;
  }
  .contact {
    position: absolute;
    left: 20px;
    top: 20px;
    font-family: "Lato", Arial, sans-serif;
    font-size: 13.5px;
    line-height: 17px;
    color: var(--ink-soft);
    letter-spacing: 0.3px;
  }
  .contact .label {
    color: var(--accent);
    font-weight: 700;
    margin-right: 3px;
  }
  .contact .online { margin-top: 9px; }
  .icon-mail {
    width: 13px;
    height: 10px;
    vertical-align: -1px;
    margin-right: 3px;
  }
  .signature {
    position: absolute;
    left: 20px;
    bottom: 24px;
    font-family: "Lato", Arial, sans-serif;
    color: var(--ink-soft);
  }
  .signature-name {
    font-weight: 700;
    font-size: 22px;
  }
  .signature-role {
    font-size: 15px;
    margin-left: 4px;
  }
</style>
</head>
<body>
<main class="sheet">
  <section class="card card-front">
    <div class="brand">
      <span class="brand-mark"></span>
      <div class="brand-name">Benedict L. Morrow Law</div>
      <div class="brand-tagline">DUI - Criminal Defense - 420</div>
    </div>
  </section>

  <section class="card card-back">
    <div class="contact">
      <div><span class="label">T</span>510-555-0183</div>
      <div><span class="label">F</span>510-555-0147</div>
      <div>735 Linden Avenue Suite 400, Oakland, CA 94612</div>
      <div class="online">
        <div>
          <svg class="icon-mail" viewBox="0 0 13 10" aria-hidden="true">
            <rect x="0" y="0" width="13" height="10" fill="var(--ink-soft)"/>
            <path d="M0.5 0.5 L6.5 5.5 L12.5 0.5" fill="none" stroke="var(--back-bg)" stroke-width="1.2"/>
          </svg>benmorrowlaw@examplemail.test
        </div>
        <div>www.benmorrowlaw.test</div>
      </div>
    </div>
    <div class="signature">
      <span class="signature-name">Ben Morrow</span><span class="signature-role">/ Attorney</span>
    </div>
  </section>
</main>
</body>
</html>
```